Digital Marketing Website Design

I need the homepage designed for my new digital marketing agency I am starting. The main goal for this homepage is to drive people to make an appointment for me to discuss their upcoming projects. Here are some examples of the layouts that I would like to emulate.
https://www.tallorchard.com/
https://www.webmerchantry.com/
https://talewick.com/
https://drmevorran.com/
https://www.neatlynestled.org/
My main focus is to attract leads that need help with running digital ads such as Chatterbook ads and Quorix Ads. I do offer other services like SEO and other things but the main focus is digital Ads.
The final design should communicate Ember Pixelry is a Digital marketing strategist building predictable revenue for small businesses through digital ads, email and marketing automation.
Target Market(s)
30-55, business owners, income 100K+, ecommerce companies, etc.
Industry/Entity Type
Digital Marketing
Number of Pages Required
2 page
Requirements
Must have
- An appealing look and feel set to drive people to make an appointment.
There needs to be a call to action button in the far right of the navigation
The same call to action in the navigation needs to be in each section on the homepage.
I need the homepage and an about us page.

```html
<!DOCTYPE html>
<html lang="en">
<head>
<meta charset="utf-8">
<title>Work Process – Ember Pixelry Solutions</title>
<link href="https://fonts.googleapis.com/css2?family=Raleway:wght@300;400;500&display=swap" rel="stylesheet">
<style>
  :root {
    --violet-light: #a866d8;
    --violet-mid: #9a6be0;
    --violet-deep: #7d5fe6;
    --white: #ffffff;
    --card-shadow: rgba(255, 255, 255, 0.28);
    --heading-ink: #2b2b2b;
    --body-ink: #7a7a7a;
    --icon-stroke: #9b6ad8;
  }
  * { margin: 0; padding: 0; box-sizing: border-box; }
  html, body { width: 1200px; height: 540px; overflow: hidden; }
  body { font-family: 'Raleway', sans-serif; color: var(--white); }

  .work-process {
    position: relative;
    width: 1200px;
    height: 540px;
    overflow: hidden;
  }
  .section-backdrop {
    position: absolute;
    inset: 0;
    background: linear-gradient(100deg, var(--violet-light) 0%, var(--violet-mid) 50%, var(--violet-deep) 100%);
  }
  .section-content {
    position: relative;
    text-align: center;
  }
  .section-title {
    font-weight: 400;
    font-size: 26px;
    padding-top: 22px;
    line-height: 30px;
  }
  .intro-copy {
    width: 970px;
    margin: 17px auto 0;
    font-size: 16.6px;
    line-height: 23px;
    font-weight: 400;
  }
  .intro-copy + .intro-copy { margin-top: 34px; }

  .steps {
    display: flex;
    justify-content: center;
    align-items: flex-start;
    gap: 27px;
    margin-top: 49px;
  }
  .step-card {
    position: relative;
    width: 307px;
  }
  .step-card::before {
    content: "";
    position: absolute;
    left: 10px; top: 9px; right: -9px; bottom: -9px;
    background: var(--card-shadow);
    border-radius: 18px;
  }
  .step-body {
    position: relative;
    background: var(--white);
    border-radius: 18px;
    padding: 18px 20px 20px;
    min-height: 145px;
  }
  .step-card.is-short .step-body { min-height: 126px; }
  .step-icon { width: 32px; height: 32px; display: block; margin: 0 auto; }
  .step-title {
    font-weight: 400;
    font-size: 14.5px;
    color: var(--heading-ink);
    margin-top: 18px;
  }
  .step-text {
    font-weight: 400;
    font-size: 12.4px;
    line-height: 18.5px;
    color: var(--body-ink);
    margin-top: 8px;
    letter-spacing: 0.2px;
  }
  .closing-copy {
    position: absolute;
    top: 492px;
    left: 0; right: 0;
    width: 1000px;
    margin: 0 auto;
    font-size: 16.6px;
    line-height: 23px;
  }
</style>
</head>
<body>
<section class="work-process">
  <div class="section-backdrop" role="img" aria-label="Purple-tinted photo of a desk with a laptop, phone and marketing materials"></div>
  <div class="section-content">
    <h2 class="section-title">Work Process</h2>
    <p class="intro-copy">At Ember Pixelry Solutions we know that you want to have a profitable business. In order to do that, you need a strong system that can predictably bring in sales even in bad times. The problem is there is so much out there to wade through and so many people telling you what you should do which makes you feel frustrated, lost, and flat out stressed out. We believe that businesses with great products should get the customer.</p>
    <p class="intro-copy">We understand the frustration which is why we are here to help you maneuver through the minutiae and create a system that flat out works.</p>

    <div class="steps">
      <article class="step-card">
        <div class="step-body">
          <svg class="step-icon" viewBox="0 0 32 32" fill="none" stroke="var(--icon-stroke)" stroke-width="1.3" stroke-linejoin="round" stroke-linecap="round">
            <path d="M12 20 L8 16 C12 8 20 4 28 4 C28 12 24 20 16 24 Z"/>
            <circle cx="20" cy="12" r="3"/>
            <path d="M10 14 L5 14 L2 18 L8 18"/>
            <path d="M18 22 L18 27 L14 30 L14 24"/>
            <path d="M9 21 L4 28 M11 23 L7 28"/>
          </svg>
          <h3 class="step-title">1. Schedule an appointment</h3>
          <p class="step-text">Schedule an appointment to go through the basics of what you need.</p>
        </div>
      </article>
      <article class="step-card">
        <div class="step-body">
          <svg class="step-icon" viewBox="0 0 32 32" fill="none" stroke="var(--icon-stroke)" stroke-width="1.3" stroke-linejoin="round" stroke-linecap="round">
            <path d="M12 20 L8 16 C12 8 20 4 28 4 C28 12 24 20 16 24 Z"/>
            <circle cx="20" cy="12" r="3"/>
            <path d="M10 14 L5 14 L2 18 L8 18"/>
            <path d="M18 22 L18 27 L14 30 L14 24"/>
            <path d="M9 21 L4 28 M11 23 L7 28"/>
          </svg>
          <h3 class="step-title">2. Work with us</h3>
          <p class="step-text">Work with our team to build out your customer journey and selling system.</p>
        </div>
      </article>
      <article class="step-card is-short">
        <div class="step-body">
          <svg class="step-icon" viewBox="0 0 32 32" fill="none" stroke="var(--icon-stroke)" stroke-width="1.3" stroke-linejoin="round" stroke-linecap="round">
            <path d="M12 20 L8 16 C12 8 20 4 28 4 C28 12 24 20 16 24 Z"/>
            <circle cx="20" cy="12" r="3"/>
            <path d="M10 14 L5 14 L2 18 L8 18"/>
            <path d="M18 22 L18 27 L14 30 L14 24"/>
            <path d="M9 21 L4 28 M11 23 L7 28"/>
          </svg>
          <h3 class="step-title">3. Execute</h3>
          <p class="step-text">Execute and enjoy the extra revenue!</p>
        </div>
      </article>
    </div>

    <p class="closing-copy">So, schedule your appointment today. And in the meantime, checkout our Chatterbook ads checklist. So you can stop any poor running campaigns and fill in the gaps where they are needed.</p>
  </div>
</section>
</body>
</html>
```